Birch Flooring Supply

Basic one-sided business card design using the attached logo. Vintage americana theme. Font is modified Arial Nova Cond, but anything that coordinates can be used

```html
<!DOCTYPE html>
<html lang="en">
<head>
<meta charset="UTF-8">
<title>Birch Flooring Supply – Business Card</title>
<link href="https://fonts.googleapis.com/css2?family=Jost:wght@400;600&display=swap" rel="stylesheet">
<style>
  :root {
    --backdrop: #2e2e2e;
    --card: #060606;
    --gold: #b39673;
    --ink: #f1ede7;
  }
  * { margin: 0; padding: 0; box-sizing: border-box; }
  html, body {
    width: 1200px; height: 900px; overflow: hidden;
    background: var(--backdrop);
  }
  .business-card {
    position: absolute;
    left: 100px; top: 164px;
    width: 1000px; height: 572px;
    background: var(--card);
    border-radius: 0 96px 0 96px;
    font-family: "Jost", sans-serif;
    color: var(--ink);
  }
  .contact-block {
    position: absolute;
    left: 72px; top: 196px;
    width: 420px;
  }
  .person-name {
    font-weight: 600;
    font-size: 30px;
    letter-spacing: 1px;
    color: var(--gold);
    text-transform: uppercase;
    line-height: 1.1;
  }
  .person-title {
    font-size: 26px;
    margin-top: 2px;
  }
  .contact-list {
    list-style: none;
    margin-top: 26px;
  }
  .contact-list li {
    display: flex; align-items: center; gap: 16px;
    font-size: 24px;
    line-height: 42px;
  }
  .contact-icon { width: 22px; height: 22px; flex: none; }
  .divider {
    height: 1px;
    background: var(--gold);
    margin: 14px 0 16px;
    width: 400px;
  }
  .address { font-size: 26px; line-height: 34px; }
  .brand-mark {
    position: absolute;
    right: 70px; top: 50%;
    transform: translateY(-50%);
    display: flex; align-items: center; gap: 16px;
  }
  .brand-dot {
    width: 22px; height: 22px; border-radius: 50%;
    background: var(--gold);
  }
  .brand-name {
    font-family: "Jost", sans-serif;
    font-weight: 600;
    font-size: 34px;
    color: var(--ink);
    text-transform: uppercase;
    letter-spacing: 1px;
    line-height: 1.1;
    width: 240px;
  }
</style>
</head>
<body>
  <div class="business-card">
    <div class="contact-block">
      <p class="person-name">Daniel Hale</p>
      <p class="person-title">Director</p>
      <ul class="contact-list">
        <li>
          <svg class="contact-icon" viewBox="0 0 24 24" fill="none" stroke="var(--gold)" stroke-width="2" stroke-linecap="round" stroke-linejoin="round"><path d="M22 16.9v3a2 2 0 0 1-2.2 2 19.8 19.8 0 0 1-8.6-3.1 19.5 19.5 0 0 1-6-6A19.8 19.8 0 0 1 2.1 4.2 2 2 0 0 1 4.1 2h3a2 2 0 0 1 2 1.7c.1 1 .4 1.9.7 2.8a2 2 0 0 1-.5 2.1L8 9.9a16 16 0 0 0 6 6l1.3-1.3a2 2 0 0 1 2.1-.4c.9.3 1.8.6 2.8.7a2 2 0 0 1 1.7 2z"/></svg>
          +1 555-014-2290
        </li>
        <li>
          <svg class="contact-icon" viewBox="0 0 24 24" fill="var(--gold)"><path d="M2 5h20v14H2z"/><path d="M2 5l10 8 10-8" fill="none" stroke="var(--card)" stroke-width="1.8"/></svg>
          hello@birchflooringsupply.com
        </li>
        <li>
          <svg class="contact-icon" viewBox="0 0 24 24" fill="none" stroke="var(--gold)" stroke-width="1.8"><circle cx="12" cy="12" r="10"/><path d="M2 12h20M12 2a15 15 0 0 1 0 20M12 2a15 15 0 0 0 0 20"/></svg>
          www.birchflooringsupply.com
        </li>
      </ul>
      <div class="divider"></div>
      <p class="address">2140 Cedar Ln , Elmwood, MN<br>United States, Minnesota</p>
    </div>
    <div class="brand-mark">
      <span class="brand-dot"></span>
      <span class="brand-name">Birch Flooring Supply</span>
    </div>
  </div>
</body>
</html>
```